A Referral Pad for a Specialist Surgeon to give to referring GPs

A referral pad allows general practitioners to easily refer patients to me by quickly filling in a form on a small pad that I provide them.

A two sided referral pad themed appropriately. Theming and designing the pad should be based on the general design/logo/imagery/colours etc. from my website www.marcusbelwether.com.au. I have a logo uploaded that should be used somewhere. I have also upload a headshot of myself which might or might not be used. Other choice of imagery and design features is up to the designer.

In terms of size of the pad I’m not quite sure what is best and will leave it up to the designers.

MORE DETAILED INFORMATION IS PROVIDED IN THE UPLOADED WORD FILE

Target Market(s)

General Practitioners referring to me

Industry/Entity Type

Healthcare

Contact Information for Business Card

A business card themed as per the referral pad design as as per general look and imagery found on www.marcusbelwether.com.au

Requirements
Must have
• Referral pad details found in uploaded Word document
Nice to have
Should not have

```html
<!DOCTYPE html>
<html lang="en">
<head>
<meta charset="utf-8">
<title>Marcus Belwether – Patient Referral Pad</title>
<link href="https://fonts.googleapis.com/css2?family=Cinzel:wght@400;600&family=Source+Sans+3:ital,wght@0,400;0,600;1,400&display=swap" rel="stylesheet">
<style>
  :root{
    --teal:#1b7b70;
    --teal-light:#5fa89f;
    --tint:#e8f1ef;
    --ink:#2b2b2b;
    --rule:#6a6a6a;
    --paper:#ffffff;
    --backdrop:#ece7df;
  }
  *{box-sizing:border-box;margin:0;padding:0}
  html,body{width:1200px;height:1200px;overflow:hidden}
  body{background:var(--backdrop);position:relative;font-family:"Source Sans 3",Arial,sans-serif;color:var(--ink);font-size:10px}

  .sheet{position:absolute;width:423px;height:600px;background:var(--paper);box-shadow:0 2px 6px rgba(0,0,0,.25);overflow:hidden}
  .sheet--top{left:390px;top:3px;z-index:2}
  .sheet--left{left:3px;top:596px}
  .sheet--right{left:772px;top:596px}

  .brand{position:absolute;left:14px;top:12px;display:flex;align-items:center;gap:6px}
  .brand__mark{width:24px;height:24px;border-radius:50%;background:var(--teal)}
  .brand__name{font-family:"Cinzel",serif;font-weight:600;font-size:17px;color:var(--teal);line-height:1}
  .brand__role{position:absolute;left:44px;top:36px;font-family:"Cinzel",serif;font-size:6.3px;letter-spacing:.6px;color:#555}

  .contact{position:absolute;left:236px;top:12px;font-size:8.6px;line-height:15px}
  .contact li{list-style:none;display:flex;align-items:center;gap:3px}
  .contact svg{width:9px;height:9px;fill:var(--teal)}

  .title-band{position:absolute;left:0;right:0;top:59px;height:17px;background:var(--teal);color:#fff;text-align:center;font-family:"Cinzel",serif;font-size:11px;line-height:17px;letter-spacing:.5px}

  .tab{position:absolute;left:0;width:132px;height:10px;background:var(--teal-light);color:#fff;font-family:"Cinzel",serif;font-size:7.6px;line-height:10px;padding-left:16px;letter-spacing:.3px}

  .row{position:absolute;display:flex;align-items:baseline;gap:4px;font-size:10px;line-height:12px}
  .rule{flex:1;border-bottom:1px solid var(--rule);height:9px;position:relative}
  .hint{position:absolute;left:45px;top:-1px;font-size:8px;color:#c9cfcd}

  .med-label{position:absolute;left:16px;top:176px;color:var(--teal);font-size:9.5px;line-height:12px}
  .med-box{position:absolute;left:12px;right:13px;top:192px;height:86px;background:var(--tint);border-radius:3px}

  .stamp{position:absolute;left:282px;top:294px;width:128px;height:97px;border:1px solid #777;border-radius:3px;text-align:center;font-size:6px;color:#ccc;padding-top:2px}

  .choice{position:absolute;left:16px;display:flex;align-items:center;gap:6px;font-size:10px;line-height:12px}
  .box{width:11px;height:11px;border:1px solid #666}
  .choice em{font-size:9.5px}
  .sub{position:absolute;left:50px;display:flex;align-items:baseline;font-size:9.5px;width:210px}
  .sub .rule{flex:none;width:104px;margin-left:auto;height:8px}

  .note-box{position:absolute;left:294px;top:534px;width:112px;height:37px;border:1px solid #888;border-radius:4px;font-size:6.6px;font-style:italic;line-height:10px;padding:3px 6px}
  .note-inline{font-size:5.6px;font-style:italic}
  .note-line{position:absolute;left:32px;top:566px;font-size:6.8px;font-style:italic}

  .footer{position:absolute;left:0;right:0;bottom:0;height:18px;background:var(--teal);color:#fff;text-align:center;font-size:9px;line-height:18px}
</style>
</head>
<body>

<section class="sheet sheet--top" aria-label="Patient referral form">
  <div class="brand"><span class="brand__mark"></span><span class="brand__name">Marcus Belwether</span></div>
  <div class="brand__role">General, Upper GI &amp; Bariatric Surgeon</div>
  <ul class="contact">
    <li><svg viewBox="0 0 10 10"><path d="M1 3c0-1 1-2 4-2s4 1 4 2v1H7V3H3v1H1z M2 5h6l1 4H1z"/></svg>(03) 9000 4182</li>
    <li><svg viewBox="0 0 10 10"><path d="M3 1h4v2H3z M1 4h8v4H7v1H3V8H1z"/></svg>(03) 9000 4183</li>
    <li><svg viewBox="0 0 10 10"><path d="M1 3h8v6H1z M1 3l4 3 4-3" fill="none" stroke="#1b7b70"/></svg>info@baysideweightsurgery.com.au</li>
  </ul>
  <div class="title-band">Patient Referral</div>

  <div class="tab" style="top:90px">Patient Information</div>
  <div class="row" style="left:298px;width:100px;top:92px">Date <span class="rule"></span></div>
  <div class="row" style="left:16px;right:22px;top:110px">Name: <span class="rule"></span></div>
  <div class="row" style="left:16px;width:215px;top:130px">DOB: <span class="rule"><span class="hint">DD/MMM/YYYY</span></span></div>
  <div class="row" style="left:234px;right:22px;top:130px">Gender: <span class="rule"></span></div>
  <div class="row" style="left:16px;width:148px;top:150px">Phone:<span class="rule"></span></div>
  <div class="row" style="left:170px;right:22px;top:150px">e-mail: <span class="rule"></span></div>
  <div class="med-label">Medical history</div>
  <div class="med-box"></div>

  <div class="tab" style="top:289px">Referring Doctor</div>
  <div class="row" style="left:18px;width:252px;top:308px">Name: <span class="rule"></span></div>
  <div class="row" style="left:18px;width:252px;top:328px">Phone: <span class="rule"></span></div>
  <div class="row" style="left:18px;width:252px;top:348px">Clinic Address: <span class="rule"></span></div>
  <div class="row" style="left:18px;width:252px;top:368px"><span class="rule"></span></div>
  <div class="stamp">Seal/ Stamp</div>

  <div class="tab" style="top:389px">Procedure Choice</div>
  <div class="choice" style="top:408px"><span class="box"></span>Bariatric Surgery <em>(details &amp; eligibility overleaf)</em></div>
  <div class="sub" style="top:425px">a. Patient Weight (Kgs):</div>
  <div class="sub" style="top:442px">b. Patient BMI: <span class="rule"></span></div>
  <div class="sub" style="top:459px">c. Diabetic? [Yes/No]: <span class="rule"></span></div>
  <div class="choice" style="top:479px"><span class="box"></span>Abdominoplasty or Arm Reduction after weight loss</div>
  <div class="choice" style="top:496px"><span class="box"></span>Antireflux/Hiatus Hernia Surgery</div>
  <div class="choice" style="top:513px"><span class="box"></span>Gallbladder</div>
  <div class="choice" style="top:530px"><span class="box"></span>Hernia</div>
  <div class="choice" style="top:547px"><span class="box"></span>Endoscopy</div>
  <div class="choice" style="top:564px"><span class="box"></span>Other general surgery*</div>
  <div class="note-box">*Includes skin, lumps &amp; bumps, peri-anal/haemorrhoids, varicose veins, carpal tunnel</div>
  <div class="footer">www.marcusbelwether.com.au</div>
</section>

<section class="sheet sheet--left" aria-label="Patient referral form, inline footnote version">
  <div class="brand"><span class="brand__mark"></span><span class="brand__name">Marcus Belwether</span></div>
  <div class="brand__role">General, Upper GI &amp; Bariatric Surgeon</div>
  <ul class="contact">
    <li><svg viewBox="0 0 10 10"><path d="M1 3c0-1 1-2 4-2s4 1 4 2v1H7V3H3v1H1z M2 5h6l1 4H1z"/></svg>(03) 9000 4182</li>
    <li><svg viewBox="0 0 10 10"><path d="M3 1h4v2H3z M1 4h8v4H7v1H3V8H1z"/></svg>(03) 9000 4183</li>
    <li><svg viewBox="0 0 10 10"><path d="M1 3h8v6H1z M1 3l4 3 4-3" fill="none" stroke="#1b7b70"/></svg>info@baysideweightsurgery.com.au</li>
  </ul>
  <div class="title-band">Patient Referral</div>

  <div class="tab" style="top:90px">Patient Information</div>
  <div class="row" style="left:298px;width:100px;top:92px">Date <span class="rule"></span></div>
  <div class="row" style="left:16px;right:22px;top:110px">Name: <span class="rule"></span></div>
  <div class="row" style="left:16px;width:215px;top:130px">DOB: <span class="rule"><span class="hint">DD/MMM/YYYY</span></span></div>
  <div class="row" style="left:234px;right:22px;top:130px">Gender: <span class="rule"></span></div>
  <div class="row" style="left:16px;width:148px;top:150px">Phone:<span class="rule"></span></div>
  <div class="row" style="left:170px;right:22px;top:150px">e-mail: <span class="rule"></span></div>
  <div class="med-label">Medical history</div>
  <div class="med-box"></div>

  <div class="tab" style="top:289px">Referring Doctor</div>
  <div class="row" style="left:18px;width:252px;top:308px">Name: <span class="rule"></span></div>
  <div class="row" style="left:18px;width:252px;top:328px">Phone: <span class="rule"></span></div>
  <div class="row" style="left:18px;width:252px;top:348px">Clinic Address: <span class="rule"></span></div>
  <div class="row" style="left:18px;width:252px;top:368px"><span class="rule"></span></div>
  <div class="stamp">Seal/ Stamp</div>

  <div class="tab" style="top:389px">Procedure Choice</div>
  <div class="choice" style="top:408px"><span class="box"></span>Bariatric Surgery <em class="note-inline">(details &amp; eligibility overleaf)</em></div>
  <div class="sub" style="top:425px">a. Patient Weight (Kgs):</div>
  <div class="sub" style="top:442px">b. Patient BMI: <span class="rule"></span></div>
  <div class="sub" style="top:459px">c. Diabetic? [Yes/No]: <span class="rule"></span></div>
  <div class="choice" style="top:479px"><span class="box"></span>Abdominoplasty or Arm Reduction after weight loss</div>
  <div class="choice" style="top:496px"><span class="box"></span>Antireflux/Hiatus Hernia Surgery</div>
  <div class="choice" style="top:513px"><span class="box"></span>Gallbladder</div>
  <div class="choice" style="top:530px"><span class="box"></span>Hernia</div>
  <div class="choice" style="top:547px"><span class="box"></span>Endoscopy</div>
  <div class="choice" style="top:564px"><span class="box"></span>Other general surgery <span class="note-inline">(Includes skin, lumps &amp; bumps, peri-anal/haemorrhoids, varicose veins, carpal tunnel)</span></div>
  <div class="footer">www.marcusbelwether.com.au</div>
</section>

<section class="sheet sheet--right" aria-label="Patient referral form, footnote line version">
  <div class="brand"><span class="brand__mark"></span><span class="brand__name">Marcus Belwether</span></div>
  <div class="brand__role">General, Upper GI &amp; Bariatric Surgeon</div>
  <ul class="contact">
    <li><svg viewBox="0 0 10 10"><path d="M1 3c0-1 1-2 4-2s4 1 4 2v1H7V3H3v1H1z M2 5h6l1 4H1z"/></svg>(03) 9000 4182</li>
    <li><svg viewBox="0 0 10 10"><path d="M3 1h4v2H3z M1 4h8v4H7v1H3V8H1z"/></svg>(03) 9000 4183</li>
    <li><svg viewBox="0 0 10 10"><path d="M1 3h8v6H1z M1 3l4 3 4-3" fill="none" stroke="#1b7b70"/></svg>info@baysideweightsurgery.com.au</li>
  </ul>
  <div class="title-band">Patient Referral</div>

  <div class="tab" style="top:90px">Patient Information</div>
  <div class="row" style="left:298px;width:100px;top:95px">Date <span class="rule"></span></div>
  <div class="row" style="left:16px;right:22px;top:113px">Name: <span class="rule"></span></div>
  <div class="row" style="left:16px;width:215px;top:133px">DOB: <span class="rule"><span class="hint">DD/MMM/YYYY</span></span></div>
  <div class="row" style="left:234px;right:22px;top:133px">Gender: <span class="rule"></span></div>
  <div class="row" style="left:16px;width:148px;top:153px">Phone:<span class="rule"></span></div>
  <div class="row" style="left:170px;right:22px;top:153px">e-mail: <span class="rule"></span></div>
  <div class="med-label" style="top:177px">Medical history</div>
  <div class="med-box" style="top:193px;height:91px"></div>

  <div class="tab" style="top:293px">Referring Doctor</div>
  <div class="row" style="left:18px;width:252px;top:311px">Name: <span class="rule"></span></div>
  <div class="row" style="left:18px;width:252px;top:331px">Phone: <span class="rule"></span></div>
  <div class="row" style="left:18px;width:252px;top:351px">Clinic Address: <span class="rule"></span></div>
  <div class="stamp" style="top:298px">Seal/ Stamp</div>

  <div class="tab" style="top:374px">Procedure Choice</div>
  <div class="choice" style="top:393px"><span class="box"></span>Bariatric Surgery <em>(details &amp; eligibility overleaf)</em></div>
  <div class="sub" style="top:410px">a. Patient Weight (Kgs):</div>
  <div class="sub" style="top:428px">b. Patient BMI: <span class="rule"></span></div>
  <div class="sub" style="top:445px">c. Diabetic? [Yes/No]: <span class="rule"></span></div>
  <div class="choice" style="top:463px"><span class="box"></span>Abdominoplasty or Arm Reduction after weight loss</div>
  <div class="choice" style="top:480px"><span class="box"></span>Antireflux/Hiatus Hernia Surgery</div>
  <div class="choice" style="top:497px"><span class="box"></span>Gallbladder</div>
  <div class="choice" style="top:514px"><span class="box"></span>Hernia</div>
  <div class="choice" style="top:531px"><span class="box"></span>Endoscopy</div>
  <div class="choice" style="top:548px"><span class="box"></span>Other general surgery*</div>
  <div class="note-line">*Includes skin, lumps &amp; bumps, peri-anal/haemorrhoids, varicose veins, carpal tunnel</div>
  <div class="footer">www.marcusbelwether.com.au</div>
</section>

</body>
</html>
```